Birchwood Ridge Electrical, needs business cards asap!

An electrical business, been in the trade for 10 to 12 years. Based on a partner business, names Dale Hartwick and Rk Tosel. Would like a potential logo drawn up to use on all products as well. It's a new company starting in the spring.
This is my first time using this site to make business cards. I can tell you a little about the business, I have been working as an electrician for 10 years for a company and have done courses to upgrade my skills, I'm open minded, and am very personable. Over the years I just have had it working for "the man" and want to try it on my own. I am extremely hard worker I work long hours.

again anything is so appreciative,

Thank you

Dale

Target Market(s)

Small town, contractors, other business owners,

Industry/Entity Type

Electrical

Contact Information for Business Card

Simple but classy

Font styles to use
Serif

Colors
ffc214
000000

Requirements
Must have
• Phone 705-418-9327
• Email birchwoodridgeelectrical@mailvane.net
• Address 7 Fenwick street parry sound on p2a 3k9
• Name of company ridge birchwood electrical
• Name of owners Dale Hartwick and rk tosel
• ECRA/ESA 4028167
Nice to have
• A potential logo which can be used on clothing trucks etc if no logo thats ok.

```html
<!DOCTYPE html>
<html lang="en">
<head>
<meta charset="utf-8">
<title>Birchwood Ridge Electrical — Business Card</title>
<link href="https://fonts.googleapis.com/css2?family=Arimo:wght@400&family=Tinos:wght@400&display=swap" rel="stylesheet">
<style>
  :root {
    --card-yellow: #f6c400;
    --band-black: #000000;
    --rule-olive: #6b5700;
    --ink: #000000;
    --page: #e4e4e2;
  }
  html, body {
    margin: 0;
    width: 1200px;
    height: 900px;
    overflow: hidden;
    background: var(--page);
  }
  .canvas {
    position: relative;
    width: 1200px;
    height: 900px;
    display: flex;
    align-items: center;
    justify-content: center;
  }
  .business-card {
    position: relative;
    width: 840px;
    height: 480px;
    background: var(--card-yellow);
    box-shadow: 0 6px 18px rgba(0,0,0,0.18);
    overflow: hidden;
  }
  .rule {
    position: absolute;
    left: 0;
    width: 100%;
    background: var(--rule-olive);
  }
  .rule--top { top: 28px; height: 6px; }
  .rule--under-band { top: 116px; height: 8px; }
  .name-band {
    position: absolute;
    top: 40px;
    left: 0;
    width: 100%;
    height: 68px;
    background: var(--band-black);
  }
  .company-name {
    position: absolute;
    left: 100px;
    top: 50%;
    transform: translateY(-50%);
    margin: 0;
    font-family: "Tinos", "Times New Roman", serif;
    font-weight: 400;
    font-size: 34px;
    letter-spacing: 0.5px;
    color: var(--card-yellow);
  }
  .details {
    position: absolute;
    left: 140px;
    top: 160px;
    font-family: "Arimo", Arial, sans-serif;
    color: var(--ink);
  }
  .owners {
    margin: 0;
    font-size: 30px;
    font-weight: 400;
    text-decoration: underline;
    text-underline-offset: 4px;
    text-decoration-thickness: 2px;
  }
  .licence {
    margin: 4px 0 0;
    font-size: 22px;
  }
  .contact {
    margin: 34px 0 0;
    font-size: 22px;
    line-height: 1.3;
  }
  .contact p { margin: 0; }
  .email-band {
    position: absolute;
    left: 0;
    bottom: 30px;
    width: 100%;
    height: 62px;
    background: var(--rule-olive);
    display: flex;
    align-items: center;
  }
  .email {
    margin: 0 0 0 140px;
    font-family: "Arimo", Arial, sans-serif;
    font-size: 24px;
    color: var(--card-yellow);
  }
</style>
</head>
<body>
  <main class="canvas">
    <article class="business-card">
      <div class="rule rule--top"></div>
      <header class="name-band">
        <h1 class="company-name">Birchwood Ridge Electrical</h1>
      </header>
      <div class="rule rule--under-band"></div>

      <section class="details">
        <h2 class="owners">Dale Hartwick &amp; RK Tosel</h2>
        <p class="licence">ECRA/ESA 4028167</p>
        <div class="contact">
          <p class="address">Address: 7 Fenwick street Parry Sound on p2a 3k9</p>
          <p class="phone">Phone #: 705-418-9327</p>
        </div>
      </section>

      <footer class="email-band">
        <p class="email">Email:birchwoodridgeelectrical@mailvane.net</p>
      </footer>
    </article>
  </main>
</body>
</html>
```